A professional business to business web site for a contract agency called VONTAREX.

We need a very clean, very professional web site created for business to business. It is an informational web site with 3 pages. We are a company that offers contract employee placements into primarily the pharmaceutical industry. I have attached a file that describes the company more fully.

Hi,

I'm sorry if I wasn't clear, but I need to have the HTML pages created so I can just upload the files you give me to the web hosting site.

Please let me know if you have any questions.

Thanks for working on my project!

Hello,

I didn't put this in the description, but I would need the web site set up on the web hosting site as well.  The web hosting site is abrightkettle.  I want a copy of all the files as well.

Thanks,
Miles

Reason: I'm sorry, unexpectedly, I have been very busy and I haven't been able to devote the time necessary for this. I am extending the deadline by 10 days. Thank you for your patience. Thanks.

Reason: Hi everyone, I apologize again, but everything has been so busy here that I haven't been able to give this attention. I plan to work on this over the next few days. Thanks and sorry again, Miles.

Reason: I'm sorry this is taking longer than planned. I have been extremely busy. I have increased the budget on this project. Thanks.

Target Market(s)

Large professional corporations mainly in the pharmaceutical industry. The audience is hiring decisions makers within the companies and potential job candidates/job seekers.

Industry/Entity Type

Pharmaceutical

Font styles to use
Sans Serif

Requirements
Must have
• Must have a clean look that mimics the pharmaceutical industry web sites. VERY professional.
Nice to have
• A nice picture of professional business/pharma/technical people looking like a team. Colors are listed on the attached Word document.
Should not have
• No animation. Not too busy.

```html
<!DOCTYPE html>
<html lang="en">
<head>
<meta charset="utf-8">
<title>VONTAREX — Enhancing your team</title>
<link rel="stylesheet" href="https://fonts.googleapis.com/css2?family=Mulish:wght@400;600;700&family=Dawning+of+a+New+Day&display=swap">
<style>
  :root {
    --navy: #1f2f7a;
    --green: #0e8a6e;
    --text: #666666;
    --text-soft: #777777;
    --heading: #2b2b2b;
    --footer-bg: #f4f4f4;
    --hero-a: #6170b0;
    --hero-b: #4a5a9c;
    --line: #d9d9d9;
    --white: #ffffff;
  }
  * { box-sizing: border-box; margin: 0; padding: 0; }
  html, body { width: 1171px; height: 1200px; overflow: hidden; }
  body {
    position: relative;
    background: var(--white);
    font-family: "Mulish", sans-serif;
    color: var(--text);
  }
  .abs { position: absolute; }

  /* Header */
  .site-header {
    position: absolute; left: 0; top: 0; width: 1171px; height: 81px;
    background: linear-gradient(#ffffff, #f1f1f1);
    border-bottom: 1px solid var(--line);
  }
  .brand {
    position: absolute; left: 157px; top: 22px;
    display: flex; align-items: center; gap: 14px;
  }
  .brand-dot { width: 34px; height: 34px; border-radius: 50%; background: var(--navy); }
  .brand-name {
    font-weight: 700; font-size: 22px; letter-spacing: 5px; color: var(--navy);
  }
  .main-nav {
    position: absolute; top: 33px; left: 471px;
    font-size: 11px; letter-spacing: 1px; color: var(--text);
  }
  .main-nav span { position: absolute; white-space: nowrap; top: 0; }
  .search-box {
    position: absolute; left: 820px; top: 26px; width: 195px; height: 30px;
    border: 1px solid var(--line); border-radius: 8px; background: var(--white);
    display: flex; align-items: center; padding-left: 10px; gap: 12px;
    font-size: 11px; color: #999;
  }

  /* Hero */
  .hero {
    position: absolute; left: 0; top: 81px; width: 1171px; height: 422px;
    background: linear-gradient(100deg, var(--hero-a), var(--hero-b) 60%, #3d4a86);
  }
  .hero-title {
    position: absolute; left: 0; width: 1171px; top: 255px; text-align: center;
    font-weight: 600; font-size: 46px; letter-spacing: 14px; color: var(--white);
  }
  .hero-tagline {
    position: absolute; left: 0; width: 1171px; top: 302px; text-align: center;
    font-family: "Dawning of a New Day", cursive; font-size: 46px; color: var(--white);
  }

  /* Intro */
  .intro-lead {
    position: absolute; left: 0; width: 1171px; top: 552px; text-align: center;
    font-size: 29px; line-height: 35px; font-weight: 400;
  }
  .intro-lead .accent { color: var(--green); display: block; }
  .intro-lead .muted { color: var(--text); display: block; }
  .intro-copy {
    position: absolute; left: 175px; width: 820px; top: 639px; text-align: center;
    font-size: 13.5px; line-height: 16px; color: var(--text-soft);
  }

  /* Services */
  .service { position: absolute; top: 717px; width: 260px; text-align: center; }
  .service-art {
    width: 120px; height: 120px; margin: 0 auto; border-radius: 10px;
    background: linear-gradient(135deg, #dfe3f1, #d7ece6);
  }
  .service-label {
    margin-top: 18px; font-size: 16px; line-height: 22px; letter-spacing: 1.5px;
    text-transform: uppercase; color: var(--text);
  }

  /* Footer */
  .site-footer {
    position: absolute; left: 0; top: 922px; width: 1171px; height: 278px;
    background: var(--footer-bg);
  }
  .footer-col { position: absolute; top: 43px; }
  .footer-col h4 { font-size: 11.5px; font-weight: 700; color: var(--heading); margin-bottom: 21px; letter-spacing: .3px; }
  .footer-col li { list-style: none; font-size: 10.5px; line-height: 19.3px; color: #444; }
  .contact-phone { font-size: 22px; color: #333; line-height: 22px; margin: -8px 0 6px; }
  .contact-line { font-size: 10.5px; line-height: 19px; color: #444; }
  .contact-line b { font-weight: 700; color: var(--heading); }
  .footer-brand {
    position: absolute; left: 171px; top: 190px;
    font-weight: 700; font-size: 19px; letter-spacing: 5px; color: var(--navy);
  }
  .copyright {
    position: absolute; top: 195px; font-size: 11.5px; color: #444; letter-spacing: .3px;
  }
  .social { position: absolute; top: 222px; display: flex; gap: 3px; align-items: center; }
  .social-btn {
    height: 17px; padding: 0 5px; background: #4a63a5; color: var(--white);
    font-size: 9.5px; font-weight: 700; line-height: 17px; border-radius: 2px;
  }
  .social-square { width: 30px; height: 20px; background: var(--white); border: 1px solid #ccc; border-radius: 2px; }
  .social-count {
    height: 18px; padding: 0 6px; border: 1px solid #bbb; background: var(--white);
    font-size: 9.5px; line-height: 16px; color: #444; border-radius: 2px;
  }
</style>
</head>
<body>

<header class="site-header">
  <div class="brand">
    <span class="brand-dot"></span>
    <span class="brand-name">VONTAREX</span>
  </div>
  <nav class="main-nav">
    <span style="left:0">OUR SERVICES</span>
    <span style="left:108px">|</span>
    <span style="left:136px">ABOUT US</span>
    <span style="left:218px">|</span>
    <span style="left:243px">CONTACT US</span>
  </nav>
  <div class="search-box">
    <svg width="16" height="16" viewBox="0 0 16 16" aria-hidden="true">
      <circle cx="6.5" cy="6.5" r="4.8" fill="none" stroke="#1f2f7a" stroke-width="2"/>
      <line x1="10" y1="10" x2="14.5" y2="14.5" stroke="#1f2f7a" stroke-width="2.4" stroke-linecap="round"/>
    </svg>
    <span>Type keywords here</span>
  </div>
</header>

<section class="hero" role="img" aria-label="Photograph of a laboratory team at work, tinted blue, with a DNA helix and a molecular diagram on the right"></section>
<div class="hero-title">VONTAREX</div>
<div class="hero-tagline">Enhancing your team</div>

<section>
  <h1 class="intro-lead">
    <span class="accent">VONTAREX specializes in offering contract professionals primarily</span>
    <span class="muted">to companies in pharmaceutical lab environments.</span>
  </h1>
  <p class="intro-copy">We look for the top people and companies to work with.&nbsp; Whether you are looking for a position, or looking for a contractor, you have come to the right place.&nbsp; We work hard to put great team members together with great teams.</p>
</section>

<section>
  <div class="service" style="left:137px">
    <div class="service-art" role="img" aria-label="Illustration of two business people shaking hands"></div>
    <div class="service-label">Client<br>Companies</div>
  </div>
  <div class="service" style="left:449px">
    <div class="service-art" role="img" aria-label="Illustration of a manager with a speech bubble of gears"></div>
    <div class="service-label">Contract Employee<br>Management</div>
  </div>
  <div class="service" style="left:759px">
    <div class="service-art" role="img" aria-label="Illustration of a magnifying glass over a person"></div>
    <div class="service-label">Seeking<br>Positions</div>
  </div>
</section>

<footer class="site-footer">
  <div class="footer-col" style="left:172px">
    <h4>Browse Our Site</h4>
    <ul><li>Home</li><li>About Us</li><li>Portfolio</li></ul>
  </div>
  <div class="footer-col" style="left:381px">
    <h4>Our Service</h4>
    <ul><li>Client Companies</li><li>Project Management</li><li>Contract employee management</li></ul>
  </div>
  <div class="footer-col" style="left:628px">
    <h4>Clients</h4>
    <ul><li>F.A.Q.</li><li>Submit Payment</li><li>Blog</li></ul>
  </div>
  <div class="footer-col" style="left:822px">
    <h4>Get in touch</h4>
    <div class="contact-phone">760-555-0182</div>
    <div class="contact-line"><b>Location:</b> 1482 Harbor Crest Lane,</div>
    <div class="contact-line">Oceanview, CA&nbsp; 92199</div>
    <div class="contact-line"><b>Email:</b> contact.us@VONTAREX.com</div>
  </div>

  <div class="footer-brand">VONTAREX</div>
  <div class="copyright" style="left:628px">Copyright 2014 © VONTAREX.com</div>
  <div class="copyright" style="left:845px">|</div>
  <div class="copyright" style="left:880px">All Rights Reserved</div>

  <div class="social" style="left:171px">
    <span class="social-btn">Like</span>
    <span class="social-btn">Share</span>
    <span class="social-count">1.1k</span>
  </div>
  <div class="social" style="left:314px">
    <span class="social-square"></span>
    <span class="social-count">2 712</span>
  </div>
</footer>

</body>
</html>
```